Timid Kitten Clinic Business Card Design

I need a business card designed for my cat only veterinary clinic. I will upload the logo that I would like included on the card. Please include:
Business Name: The Timid Kitten Clinic
Address: 4827 W. 39th Ln, Scottsdale, AZ 85317
Phone #: 480-555-6314
Website URL: www.timidkittenvet.example
And the Doctors Name: Marla Quint, DVM

```html
<!DOCTYPE html>
<html lang="en">
<head>
<meta charset="utf-8">
<title>The Timid Kitten Clinic — Business Card</title>
<link rel="stylesheet" href="https://fonts.googleapis.com/css2?family=Comfortaa:wght@500&family=Poppins:wght@400;600&display=swap">
<style>
  :root {
    --page-bg: #e6e2e2;
    --card-bg: #f6f1f1;
    --card-bg-edge: #ece4e4;
    --ink: #141010;
    --brand-green: #3f8c1e;
    --band-green: #2f7f1f;
    --band-dark: #120a06;
    --logo-fill: #3a2a55;
  }
  html, body {
    margin: 0;
    padding: 0;
    width: 1200px;
    height: 900px;
    overflow: hidden;
    background: var(--page-bg);
  }
  .business-card {
    position: absolute;
    left: 100px;
    top: 142px;
    width: 1000px;
    height: 616px;
    background: radial-gradient(ellipse at 55% 45%, var(--card-bg) 0%, var(--card-bg-edge) 100%);
    overflow: hidden;
    box-shadow: 0 6px 24px rgba(0,0,0,0.12);
  }
  .card-waves {
    position: absolute;
    inset: 0;
    width: 1000px;
    height: 616px;
  }
  .brand {
    position: absolute;
    left: 20px;
    top: 195px;
    display: flex;
    align-items: center;
    gap: 14px;
  }
  .brand-mark {
    width: 170px;
    height: 170px;
    border-radius: 50%;
    background: var(--logo-fill);
    flex: none;
  }
  .brand-name {
    margin: 0;
    font-family: "Comfortaa", sans-serif;
    font-weight: 500;
    font-size: 30px;
    line-height: 1.35;
    letter-spacing: 1.5px;
    color: var(--ink);
  }
  .contact {
    position: absolute;
    left: 538px;
    top: 172px;
    font-family: "Poppins", sans-serif;
    color: var(--ink);
  }
  .doctor-name {
    margin: 0 0 26px;
    font-weight: 600;
    font-size: 36px;
    line-height: 1.2;
    color: var(--brand-green);
    text-transform: uppercase;
  }
  .address {
    margin: 0 0 26px;
    font-style: normal;
    font-size: 27px;
    line-height: 1.3;
  }
  .contact-line {
    display: flex;
    align-items: center;
    gap: 16px;
    font-size: 27px;
    line-height: 1.35;
  }
  .contact-line.web { font-size: 26px; }
  .contact-icon {
    width: 28px;
    height: 28px;
    flex: none;
  }
</style>
</head>
<body>
  <div class="business-card">
    <svg class="card-waves" viewBox="0 0 1000 616" aria-hidden="true">
      <path class="wave-green" fill="var(--band-green)"
            d="M0,499 C150,540 350,562 536,541 C380,578 180,578 0,540 Z"/>
      <path class="wave-dark" fill="var(--band-dark)"
            d="M0,552 C180,592 390,588 560,537 C690,503 830,505 1000,538 L1000,616 L0,616 Z"/>
    </svg>

    <div class="brand">
      <div class="brand-mark" role="img" aria-label="Clinic logo emblem"></div>
      <p class="brand-name">The Timid Kitten<br>Clinic</p>
    </div>

    <div class="contact">
      <h1 class="doctor-name">Marla Quint, DVM</h1>
      <address class="address">4827 W. 39th Ln,<br>Scottsdale, AZ 85317</address>
      <div class="contact-line phone">
        <svg class="contact-icon" viewBox="0 0 24 24" aria-hidden="true">
          <path fill="var(--brand-green)" d="M6.6 2.5 9.4 6.2 7.6 8.3c1.1 2.9 3.2 5.1 6.1 6.3l2-1.9 3.8 2.7-1.4 3.6c-.4.8-1.3 1.2-2.2 1-7.1-1.6-11.9-6.5-13.3-13.6-.2-.9.2-1.8 1-2.2z"/>
          <path fill="none" stroke="var(--brand-green)" stroke-width="1.8" stroke-linecap="round" d="M14 2.8a7.5 7.5 0 0 1 7.2 7.2M13.6 6.3a4 4 0 0 1 4.1 4.1"/>
        </svg>
        <span>480-555-6314</span>
      </div>
      <div class="contact-line web">
        <svg class="contact-icon" viewBox="0 0 24 24" aria-hidden="true">
          <g fill="none" stroke="var(--brand-green)" stroke-width="1.8">
            <circle cx="12" cy="12" r="9.5"/>
            <ellipse cx="12" cy="12" rx="4.2" ry="9.5"/>
            <path d="M2.5 12h19M4 7h16M4 17h16"/>
          </g>
        </svg>
        <span>www.timidkittenvet.example</span>
      </div>
    </div>
  </div>
</body>
</html>
```